Hockey Habits Poster Board for a Girls Youth Hockey Team

I'd like to have a (2) sided poster board created for our hockey team. The poster board will be 2'x4'. There are (4) different types of team play as follows:

Offense w/Puck - You have the puck and your team is on offense
-------------
Offense wo/Puck - You do not have the puck but your teammate does
-------------
Defense on/Puck - Your opponent has the puck and you are the closest defender from your team to the opponent with the puck
-------------
Defense away/Puck - Your opponent has the puck and you are not the closes defender from your team to the opponent with the puck
--------------
Individual habits are what we want every player to have regardless of the team situation. I think I'd like to have the individual habits on both sides of the poster board.

I'm open to ideas but I thought it would be cool to have a hockey rink in the background. This is also for a girls hockey team so if you are going to use a hockey player - please make sure the player is female.

Target Market(s)

Youth Hockey

Industry/Entity Type

Youth Sports - Hockey

Font styles to use
Serif
Sans Serif

Colors
0054AA
0677BA
7BADD7
CADEEF
E8F1F8
00AB8E
00BBA5
67D7C9
C6EFE9
E9F9F6

Requirements
Must have
• All of the individual habits on both sides. All the defensive habits on one side and the offensive habits on the other side.
Nice to have
• I'd like to see an image of a hockey rink on both sides of the poster as well as a female hockey player
Should not have
• boys

```html
<!DOCTYPE html>
<html lang="en">
<head>
<meta charset="utf-8">
<title>Hockey Habits</title>
<link rel="stylesheet" href="https://fonts.googleapis.com/css2?family=Open+Sans:ital,wght@0,500;1,700;1,800&family=Arimo:wght@400&display=swap">
<style>
  :root {
    --arena-top: #070d16;
    --arena-mid: #14303f;
    --arena-glow: #3c6e80;
    --boards: #2c4a5c;
    --ice-far: #6f8d9e;
    --ice-near: #c9d8e2;
    --text: #ffffff;
    --player-blue: #1f4f9a;
    --player-dark: #1b1d24;
  }
  * { margin: 0; padding: 0; box-sizing: border-box; }
  html, body { width: 1200px; height: 600px; overflow: hidden; background: var(--arena-top); }
  .poster {
    position: relative;
    width: 1200px;
    height: 600px;
    overflow: hidden;
    color: var(--text);
    font-family: "Arimo", Arial, sans-serif;
  }
  .rink-backdrop {
    position: absolute;
    inset: 0;
    background:
      radial-gradient(ellipse 55% 22% at 50% 14%, rgba(120,170,190,0.45), transparent 70%),
      linear-gradient(180deg, var(--arena-top) 0%, var(--arena-mid) 22%, var(--arena-glow) 36%, var(--boards) 50%, var(--ice-far) 66%, var(--ice-near) 100%);
  }
  .player-photo {
    position: absolute;
    left: 60px;
    top: 219px;
    width: 328px;
    height: 292px;
    border-radius: 46% 40% 30% 38%;
    background: radial-gradient(ellipse at 45% 40%, var(--player-blue) 0%, #203a6a 45%, var(--player-dark) 80%, transparent 100%);
    opacity: 0.9;
  }
  .title {
    position: absolute;
    left: 446px;
    top: 44px;
    font-family: "Open Sans", Arial, sans-serif;
    font-weight: 500;
    font-size: 34px;
    letter-spacing: 0.2px;
  }
  .habit-grid { position: absolute; inset: 0; }
  .cell { position: absolute; width: 104px; }
  .cell h2 {
    font-family: "Open Sans", Arial, sans-serif;
    font-style: italic;
    font-weight: 800;
    font-size: 16px;
    line-height: 1;
    white-space: nowrap;
  }
  .cell p {
    font-size: 5.4px;
    line-height: 6.1px;
    margin-bottom: 3.6px;
  }
  .col-1 { left: 447px; } .col-2 { left: 634px; } .col-3 { left: 807px; } .col-4 { left: 960px; }
  .row-1 h2 { position: absolute; top: 103px; }
  .row-2 h2 { position: absolute; top: 246px; }
  .row-3 h2 { position: absolute; top: 399px; }
  .col-1.row-2 h2 { top: 247px; } .col-1.row-3 h2 { top: 400px; }
  .row-1 .copy { position: absolute; top: 124px; width: 104px; }
  .row-2 .copy { position: absolute; top: 272px; width: 104px; }
  .row-3 .copy { position: absolute; top: 435px; width: 104px; }
</style>
</head>
<body>
<main class="poster">
  <div class="rink-backdrop" role="img" aria-label="Photo of an indoor hockey arena with stadium lights and an ice rink"></div>
  <div class="player-photo" role="img" aria-label="Photo of a female hockey player in a blue jersey taking a shot"></div>

  <h1 class="title">Hockey Habits</h1>

  <section class="habit-grid">
    <div class="cell col-1 row-1"><h2>Individual</h2><div class="copy"><p>Keep your head up and your feet moving. Talk to teammates on every shift and stay ready for the puck.</p><p>Skate hard in both directions. Stick on the ice, eyes on the play. Support the puck carrier with a clear passing lane. Win your battles along the boards, finish every check and get back fast when the puck turns over. Stay calm.</p></div></div>
    <div class="cell col-2 row-1"><h2>Average</h2><div class="copy"><p>Keep your head up and your feet moving. Talk to teammates on every shift and stay ready for the puck.</p><p>Skate hard in both directions. Stick on the ice, eyes on the play. Support the puck carrier with a clear passing lane. Win your battles along the boards, finish every check and get back fast when the puck turns over. Stay calm.</p></div></div>
    <div class="cell col-3 row-1"><h2>Good</h2><div class="copy"><p>Keep your head up and your feet moving. Talk to teammates on every shift and stay ready for the puck.</p><p>Skate hard in both directions. Stick on the ice, eyes on the play. Support the puck carrier with a clear passing lane. Win your battles along the boards, finish every check and get back fast when the puck turns over. Stay calm.</p></div></div>
    <div class="cell col-4 row-1"><h2>Great</h2><div class="copy"><p>Keep your head up and your feet moving. Talk to teammates on every shift and stay ready for the puck.</p><p>Skate hard in both directions. Stick on the ice, eyes on the play. Support the puck carrier with a clear passing lane. Win your battles along the boards, finish every check and get back fast when the puck turns over. Stay calm.</p></div></div>

    <div class="cell col-1 row-2"><h2>Offense w/Puck</h2><div class="copy"><p>Keep your head up and your feet moving. Talk to teammates on every shift and stay ready for the puck.</p><p>Skate hard in both directions. Stick on the ice, eyes on the play. Support the puck carrier with a clear passing lane. Win your battles along the boards, finish every check and get back fast when the puck turns over. Stay calm.</p></div></div>
    <div class="cell col-2 row-2"><h2>Average</h2><div class="copy"><p>Keep your head up and your feet moving. Talk to teammates on every shift and stay ready for the puck.</p><p>Skate hard in both directions. Stick on the ice, eyes on the play. Support the puck carrier with a clear passing lane. Win your battles along the boards, finish every check and get back fast when the puck turns over. Stay calm.</p></div></div>
    <div class="cell col-3 row-2"><h2>Good</h2><div class="copy"><p>Keep your head up and your feet moving. Talk to teammates on every shift and stay ready for the puck.</p><p>Skate hard in both directions. Stick on the ice, eyes on the play. Support the puck carrier with a clear passing lane. Win your battles along the boards, finish every check and get back fast when the puck turns over. Stay calm.</p></div></div>
    <div class="cell col-4 row-2"><h2>Great</h2><div class="copy"><p>Keep your head up and your feet moving. Talk to teammates on every shift and stay ready for the puck.</p><p>Skate hard in both directions. Stick on the ice, eyes on the play. Support the puck carrier with a clear passing lane. Win your battles along the boards, finish every check and get back fast when the puck turns over. Stay calm.</p></div></div>

    <div class="cell col-1 row-3"><h2>Offense wo/Puck</h2><div class="copy"><p>Keep your head up and your feet moving. Talk to teammates on every shift and stay ready for the puck.</p><p>Skate hard in both directions. Stick on the ice, eyes on the play. Support the puck carrier with a clear passing lane. Win your battles along the boards, finish every check and get back fast when the puck turns over. Stay calm.</p></div></div>
    <div class="cell col-2 row-3"><h2>Average</h2><div class="copy"><p>Keep your head up and your feet moving. Talk to teammates on every shift and stay ready for the puck.</p><p>Skate hard in both directions. Stick on the ice, eyes on the play. Support the puck carrier with a clear passing lane. Win your battles along the boards, finish every check and get back fast when the puck turns over. Stay calm.</p></div></div>
    <div class="cell col-3 row-3"><h2>Good</h2><div class="copy"><p>Keep your head up and your feet moving. Talk to teammates on every shift and stay ready for the puck.</p><p>Skate hard in both directions. Stick on the ice, eyes on the play. Support the puck carrier with a clear passing lane. Win your battles along the boards, finish every check and get back fast when the puck turns over. Stay calm.</p></div></div>
    <div class="cell col-4 row-3"><h2>Great</h2><div class="copy"><p>Keep your head up and your feet moving. Talk to teammates on every shift and stay ready for the puck.</p><p>Skate hard in both directions. Stick on the ice, eyes on the play. Support the puck carrier with a clear passing lane. Win your battles along the boards, finish every check and get back fast when the puck turns over. Stay calm.</p></div></div>
  </section>
</main>
</body>
</html>
```